Harbor Lantern Bcard/Stationary
Harbor Lantern Advisory, LLC
Harbor Lantern Bcard/Stationary - Consulting
Creative Brief
Professional
Dana P. Whitcombe, AICP
Founder and Principal
4927 Corbel Street, Suite 300 Miami Beach, FL 33140
dana@harborlanternadvisory.example
https://harborlanternadvisory.example/
Please include Twitter handle on card: @msdanawhit
Include the logo either in color or in reverse. Would also like to see an option that includes the logo and this tag line: Thoughtful Plans for Growing Communities

```html
<!DOCTYPE html>
<html lang="en">
<head>
<meta charset="utf-8">
<title>Harbor Lantern Advisory — Business Card</title>
<link rel="stylesheet" href="https://fonts.googleapis.com/css2?family=Dosis:wght@500&family=Open+Sans:wght@400;600&display=swap">
<style>
  :root {
    --stage: #2b2b2d;
    --purple: #6b2a8c;
    --purple-deep: #5e2380;
    --coral: #e5543b;
    --amber: #f39a1c;
    --lime: #8dc63f;
    --white: #ffffff;
  }
  * { box-sizing: border-box; margin: 0; padding: 0; }
  html, body { width: 1200px; height: 901px; overflow: hidden; }
  body {
    background: var(--stage);
    font-family: "Open Sans", Arial, sans-serif;
    display: flex;
    flex-direction: column;
    align-items: center;
    justify-content: center;
    gap: 40px;
  }
  .card {
    width: 690px;
    height: 394px;
    position: relative;
    overflow: hidden;
  }

  /* Brand lockup */
  .brand {
    display: flex;
    align-items: center;
    gap: 14px;
  }
  .brand-dot {
    width: 44px; height: 44px;
    border-radius: 50%;
    flex: none;
  }
  .brand-text {
    font-family: "Dosis", "Arial Narrow", sans-serif;
    font-weight: 500;
    display: flex;
    flex-direction: column;
    align-items: flex-end;
    line-height: 1;
  }
  .brand-name { font-size: 36px; white-space: nowrap; }
  .brand-sub {
    font-size: 13px;
    letter-spacing: 3px;
    margin-top: 4px;
    white-space: nowrap;
  }

  /* Back of card */
  .card-back {
    background: var(--purple);
    display: flex;
    flex-direction: column;
    align-items: center;
    justify-content: center;
    color: var(--white);
  }
  .card-back .brand-dot { background: var(--white); }
  .card-back .brand-text { color: var(--white); }
  .tagline {
    margin-top: 30px;
    font-size: 14px;
    letter-spacing: 0.2px;
    white-space: nowrap;
  }

  /* Front of card */
  .card-front {
    background: var(--white);
    display: grid;
    grid-template-columns: 1fr 1fr;
  }
  .front-logo {
    display: flex;
    align-items: center;
    justify-content: center;
    padding-top: 40px;
  }
  .card-front .brand-dot { background: var(--amber); width: 38px; height: 38px; }
  .card-front .brand-text { color: var(--purple); }
  .card-front .brand-name { font-size: 31px; }
  .card-front .brand-sub { font-size: 12px; letter-spacing: 2.6px; }

  .bands {
    display: grid;
    grid-template-rows: 30% 24% 23% 23%;
    color: var(--white);
  }
  .band {
    padding: 0 22px;
    display: flex;
    flex-direction: column;
    justify-content: center;
    font-size: 13px;
    line-height: 1.45;
    white-space: nowrap;
  }
  .band-name { background: var(--purple-deep); }
  .band-address { background: var(--coral); }
  .band-reach { background: var(--amber); }
  .band-web { background: var(--lime); }
  .person {
    font-weight: 600;
    font-size: 19px;
    line-height: 1.2;
  }
  .role { font-size: 14px; }
  .line { display: flex; align-items: center; gap: 8px; }
  .line svg { width: 13px; height: 13px; flex: none; }
</style>
</head>
<body>

  <section class="card card-back" aria-label="Business card back">
    <div class="brand">
      <span class="brand-dot"></span>
      <span class="brand-text">
        <span class="brand-name">Harbor Lantern</span>
        <span class="brand-sub">ADVISORY, LLC</span>
      </span>
    </div>
    <p class="tagline">Thoughtful Plans for Growing Communities</p>
  </section>

  <section class="card card-front" aria-label="Business card front">
    <div class="front-logo">
      <div class="brand">
        <span class="brand-dot"></span>
        <span class="brand-text">
          <span class="brand-name">Harbor Lantern</span>
          <span class="brand-sub">ADVISORY, LLC</span>
        </span>
      </div>
    </div>
    <div class="bands">
      <div class="band band-name">
        <p class="person">Dana P. Whitcombe, AICP</p>
        <p class="role">Founder &amp; Principal</p>
      </div>
      <div class="band band-address">
        <p>4927 Corbel Street, Suite 300</p>
        <p>Miami Beach, FL 33140</p>
      </div>
      <div class="band band-reach">
        <p class="line">
          <svg viewBox="0 0 12 12" aria-hidden="true"><rect x="3" y="0.5" width="6" height="11" rx="1.2" fill="none" stroke="#fff" stroke-width="1.2"/><circle cx="6" cy="9.6" r="0.7" fill="#fff"/></svg>
          305-555-0148
        </p>
        <p class="line">
          <svg viewBox="0 0 12 12" aria-hidden="true"><rect x="0.6" y="2" width="10.8" height="8" fill="none" stroke="#fff" stroke-width="1.2"/><path d="M0.8 2.4 6 6.6l5.2-4.2" fill="none" stroke="#fff" stroke-width="1.2"/></svg>
          dana@harborlanternadvisory.example
        </p>
      </div>
      <div class="band band-web">
        <p class="line">
          <svg viewBox="0 0 12 12" aria-hidden="true"><circle cx="6" cy="6" r="5.2" fill="none" stroke="#fff" stroke-width="1.1"/><ellipse cx="6" cy="6" rx="2.3" ry="5.2" fill="none" stroke="#fff" stroke-width="1"/><path d="M0.8 6h10.4" stroke="#fff" stroke-width="1"/></svg>
          harborlanternadvisory.example
        </p>
        <p class="line">
          <svg viewBox="0 0 12 12" aria-hidden="true"><circle cx="6" cy="6" r="5" fill="#fff"/></svg>
          @msdanawhit
        </p>
      </div>
    </div>
  </section>

</body>
</html>
```